THE PRACTICE NAME "The Corvane MD" FOR A NEW MEDICAL PRACTICE STARTUP

THIS IS A BUSINESS CARD REQUEST FOR A KIDNEY DOCTOR's(NEPHROLOGIST) PRACTICE, THIS PRACTICE WILL BE IN EL PASO,TEXAS USA.OPEN TO INNOVATIVE IDEAS!

THE CORVANE MD ( NAME OF PRACTICE)

DEVESH R. MALHOTRA, MD FNKF FASN ( NAME OF PHYSICIAN WITH DEGREES)
BOARD CERTIFIED INTERNAL MEDICINE
BOARD CERTIFIED NEPHROLOGY
HYPERTENSION SPECIALIST

OFFICE ADDRESS, PHONE, FAX AND EMAIL PENDING

Caring for Every Step Forward.(MOTTO) THE LOGO SHOILD REFLECT THIS MESSAGE. WE NEED A LOGO DESIGN WITH 2 KIDNEYS OR CAN BE ONE KIDNEY ALSO.

Target Market(s)

PATIENTS WITH KIDNEY DISEASE, HYPERTENSION, ENGLISH AND SPANISH SPEAKING POPULATION AND PATIENTS ON DIALYSIS

Industry/Entity Type

Health Care

Contact Information for Business Card

HYPERTENSION SPECIALIST

WEBSITE URL PENDING

Font styles to use
Serif
Sans Serif
Script

Colors
fbed38
ffc214
fbf289
fbee3e
5c5c5c
333333
1b1b1b
757575
d3d3d3

Requirements
Must have
• A KIDNEY LOGO
• NAME OF THE PRACTICE
Nice to have
• IF THE CARD CAN BE IN THE SHAPE OF A KIDNEY

```html
<!DOCTYPE html>
<html lang="en">
<head>
<meta charset="utf-8">
<title>The Corvane MD – Business Card</title>
<link href="https://fonts.googleapis.com/css2?family=Crimson+Pro:wght@400&family=Open+Sans:wght@300;400;600&family=PT+Sans&display=swap" rel="stylesheet">
<style>
  :root {
    --ink-deep: #1b1b1b;
    --ink-dark: #333333;
    --ink-mid: #5c5c5c;
    --ink-icon: #757575;
    --mist: #d3d3d3;
    --white: #ffffff;
    --sun-top: #fbd02a;
    --sun-mid: #fbe45a;
    --sun-low: #fbf289;
    --swoosh: #e8e82a;
  }
  html, body {
    margin: 0;
    padding: 0;
    width: 1200px;
    height: 733px;
    overflow: hidden;
    background: var(--white);
  }
  .card {
    position: relative;
    width: 1200px;
    height: 733px;
    overflow: hidden;
    font-family: "Open Sans", Arial, sans-serif;
  }
  .card-art {
    position: absolute;
    inset: 0;
  }
  .practice-name {
    position: absolute;
    top: 20px;
    left: 140px;
    width: 800px;
    margin: 0;
    text-align: center;
    font-family: "Open Sans", Arial, sans-serif;
    font-weight: 600;
    font-size: 80px;
    letter-spacing: -1px;
    line-height: 1;
    color: var(--white);
    white-space: nowrap;
  }
  .motto {
    position: absolute;
    top: 106px;
    left: 140px;
    width: 800px;
    margin: 0;
    text-align: center;
    font-family: "PT Sans", Arial, sans-serif;
    font-size: 38px;
    line-height: 1;
    color: var(--white);
    white-space: nowrap;
  }
  .physician {
    position: absolute;
    top: 304px;
    left: 354px;
    margin: 0;
    font-family: "Crimson Pro", Georgia, serif;
    font-weight: 400;
    font-size: 43px;
    line-height: 1;
    color: var(--ink-deep);
    white-space: nowrap;
  }
  .specialty {
    position: absolute;
    top: 342px;
    left: 498px;
    margin: 0;
    font-family: "Open Sans", Arial, sans-serif;
    font-weight: 300;
    font-size: 32px;
    line-height: 1;
    color: var(--ink-deep);
    white-space: nowrap;
  }
  .contact {
    position: absolute;
    right: 346px;
    margin: 0;
    font-family: "Open Sans", Arial, sans-serif;
    font-size: 34px;
    line-height: 1;
    color: var(--ink-deep);
    white-space: nowrap;
  }
  .contact-phone { top: 428px; }
  .contact-email { top: 520px; }
  .contact-address { top: 604px; }
  .logo-name {
    position: absolute;
    top: 542px;
    left: 40px;
    width: 232px;
    margin: 0;
    text-align: center;
    font-family: "Open Sans", Arial, sans-serif;
    font-weight: 600;
    font-size: 22px;
    line-height: 1.2;
    color: var(--ink-dark);
  }
</style>
</head>
<body>
<div class="card">
  <svg class="card-art" width="1200" height="733" viewBox="0 0 1200 733" aria-hidden="true">
    <defs>
      <linearGradient id="header-shade" x1="0" y1="0" x2="0" y2="1">
        <stop offset="0" stop-color="#3a3a3a"/>
        <stop offset="1" stop-color="#111111"/>
      </linearGradient>
      <linearGradient id="sun-field" x1="0" y1="0" x2="0" y2="1">
        <stop offset="0" stop-color="var(--sun-top)"/>
        <stop offset="0.4" stop-color="var(--sun-mid)"/>
        <stop offset="1" stop-color="var(--sun-low)"/>
      </linearGradient>
    </defs>

    <rect class="header-band" x="0" y="0" width="1200" height="282" fill="url(#header-shade)"/>
    <ellipse class="header-shadow" cx="500" cy="-40" rx="620" ry="258" fill="var(--ink-deep)"/>
    <ellipse class="header-dome" cx="480" cy="-50" rx="580" ry="250" fill="#535353"/>

    <rect class="body-field" x="0" y="282" width="1200" height="451" fill="url(#sun-field)"/>
    <path class="body-swoosh" d="M240 640 C520 760 880 700 1200 496 L1200 512 C880 716 520 776 240 648 Z" fill="var(--swoosh)"/>

    <line class="name-rule" x1="362" y1="389" x2="1006" y2="389" stroke="var(--ink-deep)" stroke-width="2"/>
    <circle cx="362" cy="389" r="6" fill="var(--ink-deep)"/>
    <circle cx="1006" cy="389" r="6" fill="var(--ink-deep)"/>

    <ellipse class="icon-oval" cx="896" cy="446" rx="52" ry="36" fill="var(--white)"/>
    <ellipse class="icon-oval" cx="898" cy="538" rx="52" ry="36" fill="var(--white)"/>
    <ellipse class="icon-oval" cx="896" cy="622" rx="52" ry="36" fill="var(--white)"/>

    <path class="icon-phone" d="M880 414 L890 412 L896 430 L889 436 C892 447 899 456 907 462 L914 456 L928 467 L924 478 C914 483 898 474 888 458 C878 442 874 425 880 414 Z" fill="var(--ink-icon)"/>

    <g class="icon-mail" fill="none" stroke="var(--ink-icon)" stroke-width="2">
      <rect x="866" y="520" width="62" height="36"/>
      <path d="M866 520 L897 540 L928 520 M866 556 L892 537 M928 556 L902 537"/>
    </g>

    <path class="icon-home" d="M896 590 L926 616 L920 616 L920 654 L872 654 L872 616 L866 616 Z" fill="var(--ink-icon)"/>

    <circle class="logo-seal" cx="156" cy="556" r="116" fill="var(--mist)"/>
  </svg>

  <h1 class="practice-name">THE CORVANE MD</h1>
  <p class="motto">Caring for Every Step Forward</p>

  <p class="physician">Devesh R. Malhotra, MD FNKF FASN</p>
  <p class="specialty">Hypertension specialist</p>

  <p class="contact contact-phone">0000-0000-0000</p>
  <p class="contact contact-email">xxxxx@xxx.com</p>
  <p class="contact contact-address">City, street number. etc</p>

  <p class="logo-name">The Corvane MD</p>
</div>
</body>
</html>
```